Business Card Design

RETAIL HIGH END CONTEMPORARY WOMEN'S CLOTHING STORE
MODERN, SIMPLE, CLEAN, COOL

WE ARE ALL ABOUT NY and CALIF STYLE.... CLASSY but EDGY..
COOLEST DENIM , Trendsetting, NEUTRAL Pallettes,
Collections : Fig and Stone, Dorian Vesk, PMW, K47, QTB
Don't need names of collections on card. thats just good info
for designer of card.

WOULD LIKE THE FONT TO BE INTERESTING, but CLEAN
We are on facebook daily with photos of outfits we put together
which you can look up and friend us.... MolvaHarbor
Also on instagram .
Open to options on color and size, but need cool and fresh.

Contact Information for Business Card

DELLA 5417 Larkmoor Rd. #309 Ember Court Arcade..Va. Beach, Va. 23987
Phone 757.386.5049 Fax 757.386-2613 EMAIL..DELLAMODE@QUILLBOX.COM

```html
<!DOCTYPE html>
<html lang="en">
<head>
<meta charset="utf-8">
<title>Della Marlowe — Business Card</title>
<link rel="stylesheet" href="https://fonts.googleapis.com/css2?family=Bebas+Neue&family=Sacramento&family=PT+Sans:wght@400;700&display=swap">
<style>
  :root {
    --backdrop: #e8e5e0;
    --sky: #86cbdd;
    --sky-deep: #74c1d6;
    --ink-blue: #7ccbe0;
    --paper: #ffffff;
    --ink: #141414;
  }
  * { margin: 0; padding: 0; box-sizing: border-box; }
  html, body {
    width: 1200px;
    height: 988px;
    overflow: hidden;
    background: var(--backdrop);
  }
  .stage {
    position: relative;
    width: 1200px;
    height: 988px;
  }
  .card {
    position: absolute;
    overflow: hidden;
    background: var(--paper);
    box-shadow: 0 2px 6px rgba(0,0,0,0.12);
  }
  .card-front {
    left: 106px;
    top: 72px;
    width: 765px;
    height: 437px;
  }
  .card-back {
    left: 407px;
    top: 532px;
    width: 768px;
    height: 438px;
  }
  .pattern-field {
    position: absolute;
    inset: 0;
    background: linear-gradient(135deg, var(--sky) 0%, var(--sky-deep) 50%, var(--sky) 100%);
  }
  .card-back .pattern-field {
    clip-path: polygon(0 0, 26% 0, 81% 100%, 0 100%);
  }
  .name-disc {
    position: absolute;
    left: 112px;
    top: -48px;
    width: 534px;
    height: 534px;
    border-radius: 50%;
    background: var(--paper);
  }
  .front-name {
    position: absolute;
    left: 0;
    right: 0;
    top: 166px;
    text-align: center;
    padding-left: 12px;
    font-family: "Bebas Neue", sans-serif;
    font-size: 74px;
    letter-spacing: 3px;
    color: transparent;
    -webkit-text-stroke: 1.6px var(--ink-blue);
    white-space: nowrap;
  }
  .back-name {
    position: absolute;
    left: 392px;
    top: 54px;
    font-family: "Sacramento", cursive;
    font-size: 58px;
    color: var(--ink-blue);
    white-space: nowrap;
  }
  .contact {
    position: absolute;
    left: 108px;
    top: 148px;
    font-family: "PT Sans", sans-serif;
    font-size: 18px;
    line-height: 25px;
    color: var(--ink);
  }
  .contact-name {
    font-weight: 700;
    margin-bottom: 10px;
  }
  .contact-line {
    display: flex;
    align-items: center;
    gap: 4px;
    white-space: nowrap;
  }
  .contact-icon {
    width: 13px;
    height: 13px;
    flex: none;
  }
</style>
</head>
<body>
<main class="stage">
  <section class="card card-front">
    <div class="pattern-field" role="img" aria-label="Light blue damask heart pattern"></div>
    <div class="name-disc"></div>
    <h1 class="front-name">DELLA MARLOWE</h1>
  </section>

  <section class="card card-back">
    <div class="pattern-field" role="img" aria-label="Light blue damask heart pattern"></div>
    <p class="back-name">Della Marlowe</p>
    <address class="contact" style="font-style:normal">
      <p class="contact-name">DELLA</p>
      <p class="contact-line">5417 Larkmoor Rd. #309</p>
      <p class="contact-line">Ember Court Arcade Beach,</p>
      <p class="contact-line">Va. 23987</p>
      <p class="contact-line">
        <svg class="contact-icon" viewBox="0 0 16 16" aria-hidden="true"><path fill="currentColor" d="M3.6 1.2l2.3 2.6-1.3 1.9c.9 2 2.6 3.8 4.7 4.8l1.9-1.3 2.6 2.3-1.4 2.4C7 13.4 2.7 9 1.1 2.6z"/></svg>
        757.386.5049
      </p>
      <p class="contact-line">
        <svg class="contact-icon" viewBox="0 0 16 16" aria-hidden="true"><path fill="currentColor" d="M4 1h8v4H4zM1 6h14v6h-3v3H4v-3H1zm4 4v4h6v-4z"/></svg>
        757.386-2613 EMAIL
      </p>
      <p class="contact-line">@ DELLAMODE@QUILLBOX.COM</p>
    </address>
  </section>
</main>
</body>
</html>
```